Business Card Design Project

I need a business card design for an Organic drive thru coffee kiosk. We will serve organic coffee, teas & smoothies and will serve healthy breakfast food/snacks for people on the go.
I want the card to have 2-3 colors max (earthy colors like browns, greens and so on).
I have attached the logo I want used and would love to play off the theme of "balance."
Include:
Tidy-Kettle Coffee
address: 4820 Gorvin Ct. Raleigh, NC 27583
phone: 919-731-4062
website: www.tidy-kettle.com (website is not up yet but still include it on card)
email: Rosalind@tidy-kettle.com
I want one of the following sayings somewhere on the card (the front or back is fine):
"Eat & Drink Well, on the run!"
"Break the fast with Tidy-Kettle"
Maybe on the back list what we offer:
-Organic coffee, espresso & tea
-Blendora smoothies & protein shakes
-Zesty Pour (100% fresh local fruit and veggies)
-Tender Nibs

```html
<!DOCTYPE html>
<html lang="en">
<head>
<meta charset="utf-8">
<title>Tidy-Kettle Coffee – Business Card</title>
<link rel="stylesheet" href="https://fonts.googleapis.com/css2?family=Arimo:wght@400;700&display=swap">
<style>
  :root {
    --backdrop: #eef0f0;
    --card-yellow: #f8ef1f;
    --roast-brown: #6b3a1e;
    --ink: #2a1a10;
    --cup-tone: #5a3318;
  }
  * { box-sizing: border-box; margin: 0; padding: 0; }
  html, body {
    width: 1200px;
    height: 702px;
    overflow: hidden;
    background: var(--backdrop);
    font-family: "Arimo", Arial, sans-serif;
  }
  .stage { position: relative; width: 1200px; height: 702px; }

  .card {
    position: absolute;
    width: 480px;
    height: 274px;
    background: var(--card-yellow);
    border-left: 10px solid var(--roast-brown);
    box-shadow: 0 6px 18px rgba(0,0,0,0.12);
    color: var(--ink);
  }

  /* Front */
  .card-front { left: 560px; top: 48px; }
  .brand {
    position: absolute;
    left: 34px;
    top: 0;
    width: 200px;
    height: 100%;
    display: flex;
    align-items: center;
    gap: 10px;
  }
  .brand-dot {
    width: 22px;
    height: 22px;
    border-radius: 50%;
    background: var(--roast-brown);
    flex: none;
  }
  .brand-name {
    font-size: 30px;
    font-weight: 700;
    color: var(--roast-brown);
    white-space: nowrap;
  }
  .divider {
    position: absolute;
    left: 236px;
    top: 52px;
    width: 2px;
    height: 170px;
    background: var(--roast-brown);
  }
  .contact {
    position: absolute;
    left: 244px;
    right: 8px;
    top: 26px;
    text-align: center;
    font-weight: 700;
    font-size: 14.5px;
    line-height: 1.25;
  }
  .contact dt { margin-top: 9px; }
  .contact dt:first-child { margin-top: 0; }

  /* Back */
  .card-back { left: 200px; top: 386px; }
  .slogan {
    position: absolute;
    left: 26px;
    top: 26px;
    font-size: 19px;
    font-weight: 700;
    text-transform: uppercase;
  }
  .offer-title {
    position: absolute;
    left: 26px;
    top: 58px;
    font-size: 17px;
    font-weight: 700;
    text-transform: uppercase;
  }
  .offer-list {
    position: absolute;
    left: 26px;
    top: 92px;
    list-style: none;
    font-size: 13.5px;
    font-weight: 700;
  }
  .offer-list li {
    display: flex;
    align-items: center;
    gap: 8px;
    margin-bottom: 14px;
  }
  .offer-list li::before {
    content: "";
    width: 14px;
    height: 10px;
    border-radius: 50%;
    background: var(--roast-brown);
    flex: none;
  }
  .cup-art {
    position: absolute;
    right: 26px;
    bottom: 16px;
    width: 88px;
    height: 96px;
    border-radius: 8px;
    background: linear-gradient(180deg, rgba(90,51,24,0.15), rgba(90,51,24,0.55));
  }
</style>
</head>
<body>
<main class="stage">
  <section class="card card-front" aria-label="Card front">
    <div class="brand">
      <span class="brand-dot"></span>
      <span class="brand-name">Tidy-Kettle</span>
    </div>
    <div class="divider"></div>
    <dl class="contact">
      <dt>Address:</dt>
      <dd>4820 Gorvin Ct. Raleigh,<br>NC 27583</dd>
      <dt>Mobil:</dt>
      <dd>919-731-4062</dd>
      <dt>Email:</dt>
      <dd>Rosalind@tidy-kettle.com</dd>
      <dt>Web:</dt>
      <dd>www.tidy-kettle.com</dd>
    </dl>
  </section>

  <section class="card card-back" aria-label="Card back">
    <h2 class="slogan">Break the fast with Tidy-Kettle</h2>
    <h3 class="offer-title">We offer:</h3>
    <ul class="offer-list">
      <li>Organic coffee, espresso &amp; tea</li>
      <li>Blendora smoothies &amp; protein shakes</li>
      <li>Zesty Pour (100% fresh local fruit and veggies)</li>
      <li>Tender Nibs</li>
    </ul>
    <div class="cup-art" role="img" aria-label="Illustration of a steaming coffee cup on a saucer"></div>
  </section>
</main>
</body>
</html>
```